Dog Food Bag Packaging Redesign

Hey there..We're a small dog food company, focusing on all natural, locally sourced, high quality ingredients. They're patties, and baked for 10 min. Dogs go insane for them. We're looking to redo our packaging, and thus, its design. I've attached images. Currently, we are wrapping 12 patties in a poly bag and then butcher paper, and sticking a label on it. We're moving to a zipper seal poly that's black. I've attached the design concept from our bag manufacturer for your reference only. We don't necessarily want to use our old label, but we're not against using elements of it. We really like our current label.. I'm just not so sure it's the right call for a poly bag.We have three flavours; chicken, beef, lamb. I would LOVE to know what flavour the bag is without having to be super close to the bag. So perhaps the top part (1-4 inches) could be the flavour colour? I will have to provide some verbiage for the back. I need to add feeding instructions, and a bit of a thank you story. I'm open for suggestions on how to display ingredients/nutritional facts.

Target Market(s)

Dog Owners

Industry/Entity Type

Manufacturing

Font styles to use
Sans Serif

Colors
9bcb3c

Requirements
Must have
• Total bag design. When you submit your design, please submit your designs on top of a bag. It makes it much easier to visual the end product.
• The bag needs to have the associated flavour colours on it to differentiate flavour from a distance. Red = beef, yellow = chicken, purple = lamb.
• I'm happy with the logo being on the back only, but if on the front it needs to be small. Patties should be the main header word.
Nice to have
• I like the idea of a vertical colour bar on the side of the bag to show its flavour, but I'm not again a top horizontal bar either.
• I like PATTIES being the biggest word on the bag.

```html
<!DOCTYPE html>
<html lang="en">
<head>
<meta charset="utf-8">
<title>Hearthfield Patties – Pouch Range</title>
<link href="https://fonts.googleapis.com/css2?family=Archivo+Black&family=Archivo:wght@400;600&family=Gochi+Hand&display=swap" rel="stylesheet">
<style>
  :root {
    --canvas: #ece6e1;
    --white: #f7f7f5;
    --black: #141414;
    --ink: #2a2a2a;
    --stamp: #e5282b;
    --beef: #e8650f;
    --beef-tab: #d9725f;
    --beef-title: #d9501c;
    --chicken: #f0dc1e;
    --chicken-tab: #f0dc1e;
    --chicken-title: #7ab32e;
    --lamb: #a57ccf;
    --lamb-tab: #cfb0e3;
    --lamb-title: #8a55c2;
    --lamb-word: #b891dc;
  }
  * { box-sizing: border-box; margin: 0; padding: 0; }
  html, body { width: 1200px; height: 905px; overflow: hidden; }
  body { background: var(--canvas); font-family: "Archivo", sans-serif; position: relative; }

  .range { position: absolute; top: 120px; left: 0; width: 1200px; display: flex; justify-content: center; gap: 70px; }

  .pouch { position: relative; width: 300px; height: 480px; background: var(--white); border-radius: 6px 6px 10px 10px; overflow: hidden; box-shadow: 0 14px 30px rgba(0,0,0,.18); }

  .pouch__tab { position: absolute; top: 0; right: 28px; width: 72px; height: 74px; }
  .pouch--beef .pouch__tab { background: var(--beef-tab); }
  .pouch--chicken .pouch__tab { background: var(--chicken-tab); }
  .pouch--lamb .pouch__tab { background: var(--lamb-tab); }

  .pouch__portrait { position: absolute; top: 80px; right: 0; width: 160px; height: 240px; background: radial-gradient(ellipse at 55% 45%, #c9c9c9 0%, #e4e4e2 55%, var(--white) 85%); }

  .brand { position: absolute; top: 120px; left: 24px; display: flex; align-items: center; gap: 8px; }
  .brand__dot { width: 22px; height: 22px; border-radius: 50%; background: #6a4a35; }
  .brand__name { font-family: "Archivo", sans-serif; font-weight: 600; font-size: 17px; color: #3b3b3b; letter-spacing: .5px; }

  .title { position: absolute; top: 178px; left: 24px; right: 16px; }
  .title__kicker { font-size: 11px; letter-spacing: 2.2px; text-transform: uppercase; }
  .title__main { font-family: "Archivo Black", sans-serif; font-size: 40px; line-height: 1; text-transform: uppercase; }
  .title__flavour { font-family: "Archivo Black", sans-serif; font-size: 54px; line-height: .95; text-transform: uppercase; white-space: nowrap; }
  .pouch--chicken .title__flavour { font-size: 44px; line-height: 1.15; }

  .pouch--beef .title__kicker, .pouch--beef .title__main { color: var(--beef-title); }
  .pouch--beef .title__flavour { color: var(--beef); }
  .pouch--chicken .title__kicker, .pouch--chicken .title__main { color: var(--chicken-title); }
  .pouch--chicken .title__flavour { color: var(--chicken); }
  .pouch--lamb .title__kicker, .pouch--lamb .title__main { color: var(--lamb-title); }
  .pouch--lamb .title__flavour { color: var(--lamb-word); }

  .pouch__base { position: absolute; left: 0; bottom: 0; width: 100%; height: 160px; background: var(--black); }

  .ingredients { position: absolute; top: 316px; left: 0; width: 210px; height: 86px; padding: 7px 12px 0 24px; font-family: "Gochi Hand", cursive; font-size: 14px; line-height: 1.05; color: var(--ink); z-index: 2; }
  .pouch--beef .ingredients { background: var(--beef); }
  .pouch--chicken .ingredients { background: var(--chicken); }
  .pouch--lamb .ingredients { background: var(--lamb); }
  .ingredients__label { text-transform: uppercase; }

  .seal { position: absolute; top: 332px; right: 30px; width: 40px; height: 40px; border-radius: 50%; background: var(--black); border: 3px solid var(--stamp); z-index: 2; }

  .web { position: absolute; top: 382px; right: 14px; width: 70px; text-align: right; font-size: 10px; font-weight: 600; line-height: 1.1; z-index: 2; }
  .pouch--beef .web { color: var(--beef); }
  .pouch--chicken .web { color: var(--chicken); }
  .pouch--lamb .web { color: var(--lamb); }

  .size { position: absolute; bottom: 34px; left: 24px; font-size: 10px; color: #d8d8d8; }
  .claim { position: absolute; bottom: 34px; right: 18px; font-size: 8px; letter-spacing: .4px; text-transform: uppercase; color: #d8d8d8; }

  .stamp { position: absolute; left: 770px; top: 705px; width: 150px; height: 150px; }
</style>
</head>
<body>
  <main class="range">
    <article class="pouch pouch--beef">
      <div class="pouch__tab"></div>
      <div class="pouch__portrait" role="img" aria-label="Pencil sketch of a dog, grey tones"></div>
      <div class="brand"><span class="brand__dot"></span><span class="brand__name">HEARTHFIELD</span></div>
      <div class="title">
        <p class="title__kicker">Grass-fed beef</p>
        <p class="title__main">Patties</p>
        <p class="title__flavour">Beef</p>
      </div>
      <div class="pouch__base"></div>
      <div class="ingredients"><span class="ingredients__label">Includes:</span><br>grass fed beef, fresh eggs, apples, sweet potatoes, broccoli, carrots</div>
      <div class="seal"></div>
      <p class="web">gohearthfield<br>.ca</p>
      <p class="size">3lb (12 patties)</p>
      <p class="claim">Fresh local responsible</p>
    </article>

    <article class="pouch pouch--chicken">
      <div class="pouch__tab"></div>
      <div class="pouch__portrait" role="img" aria-label="Pencil sketch of a dog, grey tones"></div>
      <div class="brand"><span class="brand__dot"></span><span class="brand__name">HEARTHFIELD</span></div>
      <div class="title">
        <p class="title__kicker">Deboned chicken</p>
        <p class="title__main">Patties</p>
        <p class="title__flavour">Chicken</p>
      </div>
      <div class="pouch__base"></div>
      <div class="ingredients"><span class="ingredients__label">Includes:</span><br>deboned chicken, fresh eggs, apples, sweet potatoes, broccoli, carrots</div>
      <div class="seal"></div>
      <p class="web">gohearthfield<br>.ca</p>
      <p class="size">3lb (12 patties)</p>
      <p class="claim">Fresh local responsible</p>
    </article>

    <article class="pouch pouch--lamb">
      <div class="pouch__tab"></div>
      <div class="pouch__portrait" role="img" aria-label="Pencil sketch of a dog, grey tones"></div>
      <div class="brand"><span class="brand__dot"></span><span class="brand__name">HEARTHFIELD</span></div>
      <div class="title">
        <p class="title__kicker">Deboned lamb</p>
        <p class="title__main">Patties</p>
        <p class="title__flavour">Lamb</p>
      </div>
      <div class="pouch__base"></div>
      <div class="ingredients"><span class="ingredients__label">Includes:</span><br>deboned lamb, fresh eggs, apples, sweet potatoes, broccoli, carrots</div>
      <div class="seal"></div>
      <p class="web">gohearthfield<br>.ca</p>
      <p class="size">3lb (12 patties)</p>
      <p class="claim">Fresh local responsible</p>
    </article>
  </main>

  <svg class="stamp" viewBox="0 0 150 150" aria-hidden="true">
    <circle cx="75" cy="75" r="70" fill="none" stroke="var(--stamp)" stroke-width="6"/>
    <circle cx="75" cy="75" r="48" fill="none" stroke="var(--stamp)" stroke-width="3"/>
  </svg>
</body>
</html>
```